Halt and Thicken New Branding Stationary Set - updated Oct 30th 2017

Updated on 30th Oct 2017 as we now need a whole folder design instead of a folder cover. We have thought out exactly what should be on it so it wont be hard. We are happy for this to be completed only by the winning designer if you like. And also we are guaranteeing this project now. Thanks!

We just got our new logo and now we would like a stationary set so we can brand our company communications. The items we need designed are:
Business cards
Letterhead
Appointment confirmation cards
Folder - switched from folder cover. Note that if you don't wish to do this unless you are selected as the winner this is fine.

1. Business cards - for 5 employees, final names will be given once the winner is selected, but you can use this one as the sample:
Lucinda Marquez
Hair Regrowth Expert
Halt and Thicken
7182 Oakmere Ave, Suite 500
Beverly Hills CA 90299
lucinda@jamesholloway-md.example
(310) 555-0193

2. Letterhead 8.5" x 11.0" vertical
Halt and Thicken
Beverly Hills CA 90299
office@haltandthicken.example
(310) 555-0193

3. Appointment Confirmation cards - business card size
Halt and Thicken
Beverly Hills CA 90299
Appointment For:
Date:
Time:
If you are unable to make your appointment, please contact us to reschedule at:
(310) 555-0193
info@jamesholloway-md.example

*UPDATED*
4. Folder 9" x 12 " vertical with double pocket
We would like the infinity image from the logo made really big so the left side is on the back and the right side with the + sign is on the front and its takes up the maximum room on the folder.
On the front below the half logo it should say "A Biochemical Revolution..."
On the inside we would also like to have the infinity sign from the logo but faded and half on the left pocket half on the right.
On left inside pocket it should say (this will be partically written on top of the logo):
James Holloway MD
Precision Medicine
Halt and Thicken Hair
On the Right inside pocket it should say the following:
Because the Enemy of BETTER Health is Good Health
BETTER Ingredients
BETTER Recipe
BETTER Medicine
On the back below the logo on the bottom should be the contact information.
I attached a picture of our drawing of what we want for this to make it easier.

Here is our website to give you an idea of our branding: http://www.haltandthicken.example/

We are the only true cure for hair loss and need to look professional and highest quality and beyond reproach from an ethical standpoint. We are a medical clinic so this should be portrayed also.
We cured hair loss by analyzing biochemistry and rebalancing it so that the process reverses and your own hair can grow back naturally.

Business card information:

OK so here is the information for the business cards:

Lucinda Marquez
Hair Regrowth Expert
(310) 555-0193
www.haltandthicken.example

Marisol Quintero
Hair Growth Consultant
(310) 555-0193
marisol@jamesholloway-md.example
www.haltandthicken.example

Janice Pelham
CMO/COO
(310) 555-0193
janice@haltandthicken.example
www.haltandthicken.example

Dr Glen Holloway
President
(310) 555-0193
info@jamesholloway-md.example
www.haltandthicken.example

Halt and Thicken
Customer Service
(310) 555-0193
info@jamesholloway-md.example
www.haltandthicken.example

Target Market(s)

Men aged 20-24 who care about their appearance, care about their hair and care about the world.

Industry/Entity Type

Medical And Science

Font styles to use
Sans Serif

Colors
00a990
ffffff
9d9d9d
333333

Requirements
Must have
• Must use the logo and our brand colors from the logo in all designs.
• The pantone colors are:
• Green: #4ca26f
• Light Grey: #999999
• The design should be symmetrical and balanced.
Nice to have
• It should look reasonably masculine.
Should not have
• Do not include any red in the design.

```html
<!DOCTYPE html>
<html lang="en">
<head>
<meta charset="utf-8">
<title>Halt and Thicken – Business Card</title>
<link rel="stylesheet" href="https://fonts.googleapis.com/css2?family=Open+Sans:wght@400;600;700&display=swap">
<style>
  :root {
    --backdrop: #1c1c1c;
    --card-dark: #5f5f60;
    --card-light: #ffffff;
    --brand-green: #4ca26f;
    --brand-grey: #999999;
    --text-grey: #6b6b6b;
    --rule-grey: #c4c4c4;
  }
  * { box-sizing: border-box; margin: 0; padding: 0; }
  html, body {
    width: 1200px; height: 1200px; overflow: hidden;
    background: var(--backdrop);
    font-family: "Open Sans", sans-serif;
  }
  .card {
    position: absolute; left: 180px;
    width: 840px; height: 480px;
    box-shadow: 0 12px 30px rgba(0,0,0,.5);
  }
  .card--back { top: 90px; background: var(--card-dark); display: flex; align-items: center; justify-content: center; }
  .card--front { top: 630px; background: var(--card-light); display: flex; align-items: center; }

  .brand { display: flex; align-items: center; gap: 16px; }
  .brand__dot { width: 34px; height: 34px; border-radius: 50%; flex: none; }
  .brand__name { font-weight: 700; letter-spacing: .04em; text-transform: uppercase; white-space: nowrap; }

  .card--back .brand__dot { background: #ffffff; }
  .card--back .brand__name { color: #ffffff; font-size: 40px; }

  .front__logo { width: 470px; display: flex; justify-content: center; }
  .card--front .brand__dot { width: 26px; height: 26px; background: var(--brand-green); }
  .card--front .brand__name { color: var(--brand-green); font-size: 27px; }

  .front__rule { width: 1px; height: 230px; background: var(--rule-grey); }

  .contact { padding-left: 34px; color: var(--text-grey); font-size: 17px; line-height: 1.3; }
  .contact__name { color: var(--brand-green); font-weight: 700; font-size: 26px; line-height: 1.1; }
  .contact__role { margin-bottom: 18px; }
  .contact__address { margin-bottom: 18px; }
  .contact__line { display: flex; align-items: center; gap: 10px; }
  .contact__line svg { width: 14px; height: 14px; flex: none; fill: var(--brand-green); }
</style>
</head>
<body>
  <section class="card card--back">
    <div class="brand">
      <span class="brand__dot"></span>
      <span class="brand__name">Halt and Thicken</span>
    </div>
  </section>

  <section class="card card--front">
    <div class="front__logo">
      <div class="brand">
        <span class="brand__dot"></span>
        <span class="brand__name">Halt and Thicken</span>
      </div>
    </div>
    <div class="front__rule"></div>
    <div class="contact">
      <p class="contact__name">Lucinda Marquez</p>
      <p class="contact__role">Hair Regrowth Expert</p>
      <p class="contact__address">Halt and Thicken<br>7182 Oakmere Ave, Suite 500<br>Beverly Hills CA 90299</p>
      <p class="contact__line">
        <svg viewBox="0 0 24 24" aria-hidden="true"><path d="M6.6 10.8a15.1 15.1 0 0 0 6.6 6.6l2.2-2.2a1 1 0 0 1 1-.25 11.4 11.4 0 0 0 3.6.57 1 1 0 0 1 1 1V20a1 1 0 0 1-1 1A17 17 0 0 1 3 4a1 1 0 0 1 1-1h3.5a1 1 0 0 1 1 1c0 1.25.2 2.45.57 3.57a1 1 0 0 1-.25 1z"/></svg>
        (310) 555-0193
      </p>
      <p class="contact__line">
        <svg viewBox="0 0 24 24" aria-hidden="true"><path d="M2 5h20v14H2zm2 2v.5l8 5 8-5V7l-8 5z"/></svg>
        lucinda@jamesholloway-md.example
      </p>
    </div>
  </section>
</body>
</html>
```